Software company specialized in data analytics and professional services

We need a landing page design for our business. It should include our logo design. It should have multiple sections :
- stylish head
- what we do (data analytics software, professional services)
- contact form

Target Market(s)

Companies, B2B

Industry/Entity Type

Data

Number of Pages Required

1 page

Font styles to use
Sans Serif

Requirements
Must have
• Dark theme
Should not have
• Gradients on buttons

```html
<!DOCTYPE html>
<html lang="en">
<head>
<meta charset="utf-8">
<title>Korvelia — Data Analytics &amp; Professional Services</title>
<link href="https://fonts.googleapis.com/css2?family=Urbanist:wght@400;500;600;700;800;900&display=swap" rel="stylesheet">
<style>
:root{
  --magenta:#c40dc6;
  --violet:#9d12d9;
  --navy:#100747;
  --ink:#160f4a;
  --text:#1e1b33;
  --line:#c9c6d6;
  --white:#ffffff;
}
*{margin:0;padding:0;box-sizing:border-box}
html,body{width:1200px;height:2304px;overflow:hidden;background:var(--white)}
body{font-family:"Urbanist",sans-serif;color:var(--text);position:relative}
.abs{position:absolute}

/* header */
.site-header{position:absolute;left:0;top:0;width:1200px;height:60px;background:var(--white);border-bottom:1px solid #d8d8e0}
.brand{font-family:"Urbanist",sans-serif;font-weight:800;color:var(--magenta);letter-spacing:1px}
.site-header .brand{position:absolute;left:141px;top:13px;font-size:32px;line-height:34px}
.contact-item{position:absolute;top:14px;display:flex;gap:9px;align-items:center;font-size:13px;line-height:17px;color:var(--ink)}
.contact-item svg{width:28px;height:28px}

/* hero */
.hero{position:absolute;left:0;top:60px;width:1200px;height:555px;overflow:hidden}
.hero-visual{position:absolute;inset:0;background:
  radial-gradient(circle at 830px 330px,rgba(40,140,220,.55) 0,rgba(10,60,120,.35) 120px,transparent 260px),
  radial-gradient(circle at 830px 90px,rgba(30,120,200,.35) 0,transparent 120px),
  radial-gradient(ellipse at 300px 470px,rgba(20,110,170,.35) 0,transparent 380px),
  linear-gradient(180deg,#02070f 0%,#041428 70%,#072845 100%)}
.hero-curve{position:absolute;left:0;bottom:0}
.hero h1{position:absolute;left:143px;top:148px;font-size:36px;line-height:44px;font-weight:900;color:var(--white);letter-spacing:.3px}
.hero h1 span{color:var(--magenta)}
.hero p{position:absolute;left:142px;top:290px;width:365px;font-size:15.5px;line-height:23px;color:#e6ecf5}
.btn{position:absolute;display:flex;align-items:center;justify-content:center;width:166px;height:35px;border-radius:18px;background:var(--magenta);color:var(--white);font-size:13px;letter-spacing:.3px;font-weight:500}
.hero .btn{left:141px;top:360px}

/* services */
.services{position:absolute;left:0;top:650px;width:1200px;height:400px}
.eyebrow{font-size:13px;color:var(--violet)}
.section-title{font-weight:900;color:var(--ink);letter-spacing:.5px}
.services .eyebrow{position:absolute;left:143px;top:96px}
.services .section-title{position:absolute;left:143px;top:110px;font-size:41px}
.services .lead{position:absolute;left:142px;top:168px;width:360px;font-size:13.5px;line-height:19px;color:#1b1b2a}
.services .btn{left:141px;top:249px}
.network-glow{position:absolute;top:60px;left:400px;width:800px;height:260px;background:
  radial-gradient(ellipse at 15% 55%,rgba(170,185,225,.22) 0,transparent 55%),
  radial-gradient(ellipse at 92% 45%,rgba(200,170,225,.22) 0,transparent 50%)}
.service-card{position:absolute;top:57px;width:228px;height:269px;background:var(--white);border-radius:16px;box-shadow:0 8px 30px rgba(40,30,90,.1);text-align:center;padding-top:30px}
.service-card svg{width:48px;height:48px}
.service-card h3{margin-top:18px;font-size:15px;line-height:19px;font-weight:800;color:var(--ink);letter-spacing:.3px}
.service-card p{margin:15px auto 0;width:190px;font-size:12.5px;line-height:19px;color:#1b1b2a}

/* about */
.about{position:absolute;left:0;top:1073px;width:1200px;height:480px;overflow:hidden}
.about-bg{position:absolute;inset:0;background:var(--navy)}
.about-photo{position:absolute;left:0;top:0;width:620px;height:480px;background:linear-gradient(90deg,#2a3140 0%,#4c5565 45%,#2a2d55 80%,rgba(16,7,71,1) 100%)}
.about-curve{position:absolute;left:0;bottom:0}
.about-copy{position:absolute;left:609px;top:100px;width:452px;color:var(--white)}
.about-copy .eyebrow{color:var(--white)}
.about-copy h2{font-size:40px;font-weight:900;line-height:44px;letter-spacing:.6px;margin-top:2px}
.about-copy .strong{margin-top:14px;font-size:13px;line-height:19px;font-weight:700}
.about-copy p.body{margin-top:6px;font-size:13px;line-height:23px;color:#e3e0f2}

/* inquiry */
.inquiry{position:absolute;left:0;top:1630px;width:1200px;text-align:center}
.inquiry .eyebrow{color:var(--ink);font-size:13px;position:absolute;left:0;width:1200px;top:12px}
.inquiry .section-title{position:absolute;left:0;width:1200px;top:28px;font-size:28px}
.field{position:absolute;height:35px;border:1px solid var(--line);border-radius:3px;background:var(--white);font-size:13px;color:#2a2a3a;text-align:left;padding:9px 13px}
.submit{position:absolute;left:755px;top:176px;width:106px;height:70px;background:var(--violet);border-radius:0 3px 3px 0;color:var(--white);font-weight:700;font-size:15px;line-height:18px;text-align:left;padding:16px 0 0 36px}
.submit svg{position:absolute;left:12px;top:8px}

/* footer */
.site-footer{position:absolute;left:0;top:1965px;width:1200px;height:339px}
.site-footer .brand{position:absolute;left:0;width:1200px;text-align:center;top:95px;font-size:50px;color:var(--magenta)}
.footer-item{position:absolute;top:200px;display:flex;gap:14px;align-items:flex-start;color:var(--white);font-size:13px;line-height:19px}
.footer-item svg{width:32px;height:32px;margin-top:2px}
.footer-rule{position:absolute;left:141px;top:274px;width:918px;height:1px;background:#2d2666}
.copyright{position:absolute;left:142px;top:302px;color:var(--white);font-size:13px}
.socials{position:absolute;right:141px;top:292px;display:flex;gap:7px}
.socials span{display:block;width:31px;height:31px;border:1px solid var(--magenta)}
</style>
</head>
<body>

<header class="site-header">
  <div class="brand">KORVELIA</div>
  <div class="contact-item" style="left:765px">
    <svg viewBox="0 0 28 28" fill="none" stroke="#c40dc6" stroke-width="1.4"><path d="M6 4l4 5-2 3c1.5 3 4 5.5 7 7l3-2 5 4-3 3C12 24 4 16 3 7z"/><circle cx="20" cy="8" r="5"/><path d="M17.5 8l2 2 3-3.5"/></svg>
    <div>CALL US<br>+ 123 456 7890</div>
  </div>
  <div class="contact-item" style="left:910px">
    <svg viewBox="0 0 28 28" fill="none" stroke="#c40dc6" stroke-width="1.4"><path d="M3 11l11-8 11 8v14H3z"/><path d="M3 11l11 8 11-8"/><path d="M7 8h14v6"/></svg>
    <div>EMAIL US<br>info@korvelia.com</div>
  </div>
</header>

<section class="hero">
  <div class="hero-visual" role="img" aria-label="Dark technology backdrop with an open hand holding glowing holographic data icons"></div>
  <svg class="hero-curve" width="1200" height="60" viewBox="0 0 1200 60"><path d="M0 10 Q600 100 1200 10 V60 H0 Z" fill="#fff"/></svg>
  <h1>HELPING <span>BUSINESSES</span><br>SUCCEED WITH<br>IT TECHNOLOGY</h1>
  <p>Lorem ipsum dolor sit amet, consectetuer adipiscing elit, sed diam nonummy nibh euismod tincidunt.</p>
  <div class="btn">CONTACT US TODAY</div>
</section>

<section class="services">
  <div class="network-glow" role="img" aria-label="Faint connected-dots network pattern"></div>
  <div class="eyebrow">Solutions &amp; Focus Areas</div>
  <h2 class="section-title">WHAT WE DO</h2>
  <p class="lead">Lorem ipsum dolor sit amet, consectetuer adipiscing elit, sed diam nonummy nibh euismod tincidunt ut laoreet dolore magna aliquam erat volutpat.</p>
  <div class="btn">CONTACT US TODAY</div>

  <article class="service-card" style="left:558px">
    <svg viewBox="0 0 48 48" fill="none" stroke="#c40dc6" stroke-width="1.6"><rect x="4" y="6" width="40" height="28" rx="2"/><path d="M4 29h40M20 34l-2 6h12l-2-6M14 40h20"/><rect x="12" y="2" width="24" height="22"/><circle cx="19" cy="10" r="3"/><path d="M25 9h7M25 13h7M16 18h16"/></svg>
    <h3>DATA ANALYTICS<br>SOFTWARE</h3>
    <p>Lorem ipsum dolor sit amet, consectetuer adipiscing elit, sed diam nonummy nibh euismod tincidunt ut laoreet dolore magna aliquam erat volutpat.</p>
  </article>
  <article class="service-card" style="left:814px">
    <svg viewBox="0 0 48 48" fill="none" stroke="#c40dc6" stroke-width="1.6"><circle cx="24" cy="16" r="5"/><path d="M16 34c0-6 3-10 8-10s8 4 8 10M20 34v10M28 34v10"/><circle cx="24" cy="4" r="2"/><circle cx="10" cy="10" r="2"/><circle cx="38" cy="10" r="2"/><circle cx="6" cy="24" r="2"/><circle cx="42" cy="24" r="2"/><circle cx="10" cy="36" r="2"/><circle cx="38" cy="36" r="2"/><path d="M24 6v5M12 12l7 3M36 12l-7 3M8 24h8M40 24h-8"/></svg>
    <h3>PROFESSIONAL<br>SERVICES</h3>
    <p>Lorem ipsum dolor sit amet, consectetuer adipiscing elit, sed diam nonummy nibh euismod tincidunt ut laoreet dolore magna aliquam erat volutpat.</p>
  </article>
</section>

<section class="about">
  <div class="about-bg"></div>
  <div class="about-photo" role="img" aria-label="Businessman working on a laptop surrounded by holographic support and communication graphics"></div>
  <svg class="about-curve" width="1200" height="60" viewBox="0 0 1200 60"><path d="M0 13 Q600 100 1200 13 V60 H0 Z" fill="#fff"/></svg>
  <div class="about-copy">
    <div class="eyebrow">About</div>
    <h2>KORVELIA</h2>
    <p class="strong">Lorem ipsum dolor sit amet, consectetuer adipiscing elit, sed diam nonum my nibh euismod tincid unt ut laoreet dolore magna aliquam</p>
    <p class="body">Lorem ipsum dolor sit amet, consectetuer adipiscing elit, sed diam nonummy nibh euismod tincidunt ut laoreet dolore magna aliquam erat volutpat. Ut wisi enim ad minim veniam, quis nostrud exerci tation ullamcorper suscipit lobortis nisl ut aliquip ex ea commodo consequat.</p>
    <p class="body" style="margin-top:2px">Duis autem vel eum iriure dolor in hendrerit in vulputate velit esse molestie consequat, vel illum dolore eu feugiat nulla facilisis at vero eros et accumsan et iusto odio dignissim qui blandit praesent luptatum zzril delenit augue duis</p>
  </div>
</section>

<section class="inquiry">
  <div class="eyebrow">Get in Touch</div>
  <h2 class="section-title">QUICK INQUIRY</h2>
  <div class="field" style="left:340px;top:82px;width:253px">Your name*</div>
  <div class="field" style="left:607px;top:82px;width:254px">Company name*</div>
  <div class="field" style="left:340px;top:129px;width:253px">Email*</div>
  <div class="field" style="left:607px;top:129px;width:254px">Phone*</div>
  <div class="field" style="left:340px;top:176px;width:416px;height:70px;border-radius:3px 0 0 3px">Message</div>
  <div class="submit">
    <svg width="20" height="20" viewBox="0 0 20 20" fill="#fff"><path d="M2 9L18 2 13 18 10 11z"/></svg>
    SUBMIT<br>NOW
  </div>
</section>

<footer class="site-footer">
  <svg class="abs" style="left:0;top:0" width="1200" height="339" viewBox="0 0 1200 339"><path d="M0 50 Q600 -40 1200 50 V339 H0 Z" fill="#0f0745"/></svg>
  <div class="brand">KORVELIA</div>
  <div class="footer-item" style="left:141px">
    <svg viewBox="0 0 32 32" fill="none" stroke="#fff" stroke-width="1.3"><path d="M3 15L16 4l13 11M6 13v16h20V13"/><path d="M13 29v-8h6v8"/><circle cx="22" cy="20" r="4"/></svg>
    <div>123, Building Name, Street<br>City, State XY 123456</div>
  </div>
  <div class="footer-item" style="left:387px">
    <svg viewBox="0 0 28 28" fill="none" stroke="#fff" stroke-width="1.3"><path d="M6 4l4 5-2 3c1.5 3 4 5.5 7 7l3-2 5 4-3 3C12 24 4 16 3 7z"/><circle cx="20" cy="8" r="5"/><path d="M17.5 8l2 2 3-3.5"/></svg>
    <div>CALL US<br>+ 123 456 7890</div>
  </div>
  <div class="footer-item" style="left:571px">
    <svg viewBox="0 0 28 28" fill="none" stroke="#fff" stroke-width="1.3"><path d="M3 11l11-8 11 8v14H3z"/><path d="M3 11l11 8 11-8"/><path d="M7 8h14v6"/></svg>
    <div>EMAIL US<br>info@korvelia.com</div>
  </div>
  <div class="footer-item" style="left:783px">
    <svg viewBox="0 0 32 32" fill="none" stroke="#fff" stroke-width="1.3"><circle cx="17" cy="15" r="11"/><path d="M17 8v7l5 3"/><circle cx="8" cy="24" r="4"/></svg>
    <div>WORKING HOURS<br>Monday to Friday : 09.00 am to 05.30 pm</div>
  </div>
  <div class="footer-rule"></div>
  <div class="copyright">© 2023 KORVELIA. All Rights Reserved.</div>
  <div class="socials" aria-label="Social links">
    <span></span><span></span><span></span><span></span>
  </div>
</footer>

</body>
</html>
```